business card for a massage therapy practice named 'Meadow and Willow Massage Studio'

I really need a trendy, yet easy on the eyes business card to complement my logo. Ideally with some gold or rose gold foil work.

My uploaded file of the logo I have in horizontal but I have a vertical version as well. Another color that is used in the website is a blush pink here and there. I'd like to see some trendy tropical leaves in the design.

```html
<!DOCTYPE html>
<html lang="en">
<head>
<meta charset="UTF-8">
<title>Meadow and Willow Massage Studio – Business Card Back</title>
<link rel="stylesheet" href="https://fonts.googleapis.com/css2?family=Raleway:wght@400;500&display=swap">
<style>
  :root {
    --paper: #ffffff;
    --mint: #86ceb5;
    --ink-light: #ffffff;
  }
  html, body {
    margin: 0;
    padding: 0;
    width: 1200px;
    height: 720px;
    overflow: hidden;
    background: var(--paper);
  }
  .card {
    position: relative;
    width: 1200px;
    height: 720px;
    overflow: hidden;
    background: var(--paper);
    font-family: "Raleway", sans-serif;
  }
  /* open white field above the name is intentional breathing space */
  .card-field {
    position: absolute;
    left: 0;
    top: 0;
    width: 1200px;
    height: 421px;
    background: var(--paper);
  }
  .therapist-name {
    position: absolute;
    left: 101px;
    top: 353px;
    margin: 0;
    font-size: 56px;
    font-weight: 400;
    letter-spacing: 2px;
    line-height: 1;
    white-space: nowrap;
    color: var(--mint);
  }
  .contact-band {
    position: absolute;
    left: 0;
    top: 421px;
    width: 1200px;
    height: 299px;
    background: var(--mint);
  }
  .contact-list {
    list-style: none;
    margin: 0;
    padding: 0;
    position: absolute;
    left: 106px;
    top: 29px;
  }
  .contact-list li {
    font-size: 31px;
    font-weight: 500;
    letter-spacing: 1.2px;
    line-height: 49px;
    white-space: nowrap;
    color: var(--ink-light);
  }
</style>
</head>
<body>
  <div class="card">
    <div class="card-field"></div>
    <h1 class="therapist-name">Danielle Reyes LMT</h1>
    <div class="contact-band">
      <ul class="contact-list">
        <li class="contact-phone">916.555.0148</li>
        <li class="contact-email">meadowandwillow@mail.com</li>
        <li class="contact-web">www.meadowandwillow.com</li>
        <li class="contact-social">@meadowandwillow</li>
      </ul>
    </div>
  </div>
</body>
</html>
```